依頼詳細
【作製にあたって】
添付のラフ.xlsxは、おおまかなコンテンツ配置になります。(比率などはあまり気にしないでください。)
細部のデザインをよろしくお願いいたします。多少構成が変わっても問題ありません。

白ベースで明るくシンプルなデザインをお願いします。
サブカラー、ポイントカラーはイラストの雰囲気に合った色でお願いします。

サイト作製の目的は、信用度の向上、イラスト作製への問い合わせ増加を望んでいます。
ターゲットは、中年、お年寄りになりますので、ご留意下さい。

サイト幅は900-1000pxの間でお選び下さい。

ご不明な点はお気軽にご連絡下さい。
それではたくさんのご応募お待ちしております。

サイトURL
ページ数
1ページ
希望イメージ
シンプル 複雑
単色 カラフル
暗い 明るい
日常 高級
遊び心 厳粛
未来的 伝統的
女性的 男性的
希望する色
納品ファイル
• 高解像度JPG (.jpg)
• フォトショップ形式 (.psd)
補足説明
■ 選んだ理由

・全体的にイラストと雰囲気が合っているため。
・ターゲットや使う環境を考えた提案をして頂けた。
・またコメント内容がしっかりしており実績で高評価を獲得しているため

この3点が選んだ内容になります。
ありがとうございました。

■ 提案者全員のお礼・コメント

この度は多くのご提案頂き誠にありがとうございました。

またの11月ほどに新しくサイトを作製する予定がありますので、コンペにてご提案頂けますと幸いです。

今後ともよろしくお願い致します。

```html
<!DOCTYPE html>
<html lang="ja">
<head>
<meta charset="UTF-8">
<title>彩筆工房</title>
<link rel="stylesheet" href="https://fonts.googleapis.com/css2?family=Noto+Sans+JP:wght@400;700&family=Noto+Serif+JP:wght@700&display=swap">
<style>
:root{
  --orange:#e89a12;
  --ink:#333;
  --muted:#777;
  --line:#ddd;
  --cream:#f4efe2;
  --gold:#9c7c2c;
  --hero-a:#d9cfb8;
  --hero-b:#8a8f86;
}
*{margin:0;padding:0;box-sizing:border-box}
html,body{width:807px;height:1200px;overflow:hidden}
body{font-family:"Noto Sans JP",sans-serif;color:var(--ink);background:#fff;position:relative}
.site-header{height:102px;position:relative}
.brand{position:absolute;left:232px;top:10px;font-family:"Noto Serif JP",serif;font-weight:700;font-size:34px;color:var(--ink);letter-spacing:4px;display:flex;align-items:center;gap:8px}
.brand-dot{width:14px;height:14px;background:var(--orange);border-radius:50%}
.global-nav{position:absolute;top:64px;left:250px;display:flex;gap:48px}
.global-nav a{text-decoration:none;color:var(--ink);font-size:14px;font-weight:700;text-align:center;line-height:1.1}
.global-nav a span{display:block;font-size:9px;color:var(--orange);font-weight:400}
.global-nav a.current{color:var(--orange)}
.hero{height:278px;background:linear-gradient(120deg,var(--hero-a),#b8a88a 35%,var(--hero-b) 60%,#c9b37a)}
.hero-thumbs{display:flex;justify-content:center;gap:6px;margin-top:6px}
.hero-thumbs div{width:62px;height:40px;background:linear-gradient(135deg,#c7b48e,#7f8478);opacity:.8}
.hero-thumbs div.active{opacity:1;outline:2px solid var(--orange)}
.section-title{text-align:center;margin-top:22px;font-size:22px;font-weight:700;line-height:1.1}
.section-title small{display:block;font-size:11px;color:var(--orange);font-weight:400}
.profile{display:flex;gap:20px;width:550px;margin:24px auto 0}
.profile-art{width:122px;height:160px;flex:none;background:linear-gradient(160deg,#e9dcc0,#b3a07a)}
.history{flex:1;font-size:10px;line-height:1.75}
.history-row{display:flex;gap:20px;padding:4px 0 8px;border-bottom:1px dotted var(--line)}
.history-row:last-child{border-bottom:0}
.history-row dt{width:40px;flex:none}
.block-head{width:550px;margin:34px auto 0;display:flex;justify-content:space-between;align-items:flex-end;border-left:4px solid var(--orange);padding-left:8px;border-bottom:1px solid var(--line);padding-bottom:4px}
.block-head h2{font-size:14px}
.block-head h2 small{font-size:9px;color:var(--orange);font-weight:400;margin-left:4px}
.block-head a{font-size:9px;color:var(--orange);text-decoration:none}
.gallery{width:550px;margin:10px auto 0;display:flex;gap:10px}
.gallery div{flex:1;height:103px;background:linear-gradient(135deg,#d8c6a0,#8e8f80)}
.gallery div:nth-child(2){background:linear-gradient(135deg,#c9a88a,#6e6a5e)}
.gallery div:nth-child(3){background:linear-gradient(135deg,#d9b86a,#8a6a3a)}
.management{width:550px;margin:26px auto 0;border:1px solid var(--line);background:#fafafa;padding:18px 20px;display:flex;align-items:center;gap:14px;height:96px}
.management svg{flex:none}
.management h2{font-size:15px;width:170px;line-height:1.2}
.management h2 small{display:block;font-size:9px;color:var(--orange);font-weight:400}
.management p{font-size:9px;line-height:1.7;color:var(--muted);flex:1}
.site-footer{position:absolute;left:0;right:0;bottom:0;height:172px;background:var(--cream);text-align:center}
.site-footer .brand{position:static;justify-content:center;margin-top:10px;font-size:30px}
.footer-text{font-size:8px;color:var(--muted);margin-top:10px}
.footer-link{font-size:8px;color:var(--orange);margin-top:4px}
.footer-nav{font-size:9px;margin-top:12px}
.footer-nav a{color:var(--ink);text-decoration:none;margin:0 6px}
.copyright{position:absolute;left:0;right:0;bottom:0;height:18px;background:var(--gold);color:#fff;font-size:8px;line-height:18px}
</style>
</head>
<body>
<header class="site-header">
  <div class="brand"><span class="brand-dot"></span>彩筆工房</div>
  <nav class="global-nav">
    <a href="#" class="current">トップ<span>top</span></a>
    <a href="#">イラスト一覧<span>illustration</span></a>
    <a href="#">商品一覧<span>goods</span></a>
  </nav>
</header>

<div class="hero" role="img" aria-label="賑やかな街並みと人々を描いた水彩イラストのメインビジュアル"></div>
<div class="hero-thumbs">
  <div class="active" role="img" aria-label="イラストのサムネイル1"></div>
  <div role="img" aria-label="イラストのサムネイル2"></div>
  <div role="img" aria-label="イラストのサムネイル3"></div>
  <div role="img" aria-label="イラストのサムネイル4"></div>
</div>

<h1 class="section-title">プロフィール<small>profile</small></h1>
<section class="profile">
  <div class="profile-art" role="img" aria-label="作家の自画像イラスト"></div>
  <dl class="history">
    <div class="history-row"><dt>1979年</dt><dd>愛知県出身。<br>幼少期より絵を描くことが好きで、<br>身近な風景や人々をよく描いていた。<br>子供の頃の夢は絵を描く仕事でした。<br>高校卒業後、美術専門学校へ進学。<br>「絵の可能性を広げたい」<br>という思いで制作に励む。<br>卒業後はデザイン事務所に勤務し、<br>広告や書籍の挿絵を数多く手がける。</dd></div>
    <div class="history-row"><dt>2009年</dt><dd>独立し彩筆工房を開設。色鮮やかな作品を<br>制作し、現在も各地で活動を続けている。</dd></div>
  </dl>
</section>

<div class="block-head"><h2>イラスト一覧<small>illustration</small></h2><a href="#">→イラスト一覧へ</a></div>
<div class="gallery">
  <div role="img" aria-label="街の人々を描いたイラスト"></div>
  <div role="img" aria-label="室内の情景を描いたイラスト"></div>
  <div role="img" aria-label="祭りの夜を描いたイラスト"></div>
</div>

<section class="management">
  <svg width="34" height="34" viewBox="0 0 34 34"><circle cx="17" cy="17" r="16" fill="var(--orange)"/><rect x="15" y="8" width="4" height="12" rx="1" fill="#fff"/><circle cx="17" cy="25" r="2.2" fill="#fff"/></svg>
  <h2>マネジメントについて<small>management</small></h2>
  <p>彩筆工房の作品制作は、アトリエ北斗が窓口となり承っております。<br>ご依頼やご相談は下記よりお気軽にお問い合わせください。<br>http://www.hokuto-atelier.jp/<br>イラストの無断転載はご遠慮ください。</p>
</section>

<footer class="site-footer">
  <div class="brand"><span class="brand-dot"></span>彩筆工房</div>
  <p class="footer-text">イラストのご依頼・お問い合わせは下記よりお気軽にご連絡ください。</p>
  <p class="footer-link">hokuto-atelier.jp</p>
  <nav class="footer-nav"><a href="#">トップ</a>｜<a href="#">イラスト一覧</a>｜<a href="#">商品一覧</a></nav>
  <div class="copyright">Copyright © 2013 彩筆工房</div>
</footer>
</body>
</html>
```